Gently Windswept needs an eye catching marketing flyer

Our new Lumenvale Method(r) business needs an eye catching marketing flyer. We think A5 sizing?
website link (where you can understand more about breathwork is www.gentlywindswept-example.co.uk)
Design whatever you would like to design some things that could be of use to mention are below. Will leave it in your capable hands.
Logo files for Gently Windswept attached, use whichever one is best for your design, should be the main logo and colour scheme for the flyer, the second logo is that of Lumenvale Method(r) the breath school who's body of work we will be delivering. This can be anywhere on the flyer
Flyer is needed to get people interested in breathwork, the potential benefits for breathing better
We offer 1:1 sessions, workshops, corporate training
The flyer will have an offer code 'OpenDoor' which will give 15% off the bookers first 1:1 session
Flyer should include the following contact details: Maybe a "find out how breathwork can help you today. . . "
Carol Pennick (South): 07700 900 318
Rosalind Tarrow (Midlands): 07700 900 742
facebook: we.are.gentlywindswept
instagram: _gentlywindswept_

```html
<!DOCTYPE html>
<html lang="en">
<head>
<meta charset="utf-8">
<title>Gently Windswept – Breathwork Flyer</title>
<link rel="stylesheet" href="https://fonts.googleapis.com/css2?family=Montserrat:wght@400;500;600;700;800&family=Oswald:wght@500;600&display=swap">
<style>
  :root {
    --page-bg: #e4e4e2;
    --paper: #f4f4f5;
    --brand-blue: #1d3fa8;
    --deep-navy: #16275e;
    --violet: #8a6bd1;
    --teal: #3cc6c0;
    --muted: #4a4f5c;
    --badge-top: #4e5674;
    --badge-bottom: #262c45;
    --badge-ring: #7a55d6;
    --sky-deep: #1a2b6e;
    --sky-mid: #5a70c8;
    --nebula-warm: #9b5a34;
  }
  * { box-sizing: border-box; margin: 0; padding: 0; }
  html, body { width: 1200px; height: 900px; overflow: hidden; background: var(--page-bg); }
  body { font-family: "Montserrat", Arial, sans-serif; position: relative; }

  .flyer {
    position: absolute; left: 295px; top: 19px;
    width: 610px; height: 862px;
    background: var(--paper);
    overflow: hidden;
    box-shadow: 0 3px 10px rgba(0,0,0,.25);
  }
  .hero-image {
    position: absolute; left: 0; top: 0; width: 610px; height: 580px;
    background:
      radial-gradient(ellipse 40% 35% at 65% 30%, rgba(230,190,170,.85), transparent 70%),
      radial-gradient(ellipse 30% 30% at 30% 40%, rgba(120,80,200,.7), transparent 70%),
      radial-gradient(ellipse 45% 50% at 20% 70%, var(--nebula-warm), transparent 75%),
      radial-gradient(ellipse 50% 50% at 85% 60%, var(--sky-mid), transparent 75%),
      linear-gradient(160deg, var(--sky-deep), #3b4fa3 45%, #6b4a5a 80%);
  }
  .curve-layer { position: absolute; left: 0; top: 0; }

  .offer-badge {
    position: absolute; left: 389px; top: 389px;
    width: 190px; height: 190px; border-radius: 50%;
    background: radial-gradient(circle at 50% 30%, var(--badge-top), var(--badge-bottom));
    border: 4px solid var(--badge-ring);
    box-shadow: 0 12px 14px -6px rgba(0,0,0,.35);
    color: #fff; text-align: center;
    display: flex; flex-direction: column; justify-content: center; align-items: center;
  }
  .offer-badge .label { font-weight: 400; font-size: 21px; line-height: 1.1; }
  .offer-badge .code { font-weight: 700; font-size: 20px; line-height: 1.25; }
  .offer-badge .amount { font-weight: 800; font-size: 31px; line-height: 1.1; }
  .offer-badge .terms { font-weight: 500; font-size: 13px; line-height: 1.7; }

  .services { position: absolute; left: 31px; top: 438px; }
  .services h1 { font-weight: 800; font-size: 53px; color: var(--brand-blue); letter-spacing: -0.5px; line-height: 1.1; }
  .services .formats { font-weight: 700; font-size: 21px; color: var(--violet); margin-top: 8px; padding-left: 5px; }
  .services .corporate { font-weight: 700; font-size: 24px; color: var(--teal); padding-left: 5px; }

  .call-to-action { position: absolute; left: 31px; top: 592px; color: var(--deep-navy); font-weight: 800; }
  .call-to-action .line-one { font-size: 18px; }
  .call-to-action .line-two { font-size: 26px; line-height: 1.05; }

  .contacts { position: absolute; left: 31px; top: 663px; color: var(--brand-blue); font-size: 17px; line-height: 22px; }
  .contacts .name { font-weight: 600; }
  .contacts .phone { font-weight: 700; }

  .social { position: absolute; left: 33px; top: 776px; list-style: none; font-size: 12.5px; color: var(--muted); line-height: 17px; }
  .social li { display: flex; align-items: center; gap: 7px; }
  .social .dot { width: 10px; height: 10px; border-radius: 50%; background: var(--deep-navy); }

  .address { position: absolute; left: 31px; top: 810px; font-family: "Oswald", Arial, sans-serif; font-weight: 500; font-size: 11px; color: var(--deep-navy); }
  .website { position: absolute; left: 31px; top: 822px; font-family: "Oswald", Arial, sans-serif; font-weight: 600; font-size: 27px; color: var(--brand-blue); }

  .brand-mark {
    position: absolute; left: 378px; top: 672px; width: 200px; height: 180px;
    display: flex; align-items: center; justify-content: center; gap: 10px;
  }
  .brand-mark .ring { width: 14px; height: 14px; border-radius: 50%; background: var(--violet); flex: none; }
  .brand-mark .name { font-weight: 700; font-size: 24px; line-height: 1.15; color: var(--deep-navy); }
</style>
</head>
<body>
  <main class="flyer">
    <div class="hero-image" role="img" aria-label="Photo of a woman with closed eyes, breathing calmly, blended into a starry galaxy nebula"></div>

    <svg class="curve-layer" width="610" height="862" viewBox="0 0 610 862" aria-hidden="true">
      <defs>
        <linearGradient id="swoop" x1="0" y1="0" x2="1" y2="0">
          <stop offset="0" stop-color="#3cc6c0"/>
          <stop offset="0.5" stop-color="#1d3fa8"/>
          <stop offset="1" stop-color="#8a6bd1"/>
        </linearGradient>
      </defs>
      <path d="M0 383 C 150 350, 330 380, 610 560 L610 862 L0 862 Z" fill="#f4f4f5"/>
      <path d="M0 383 C 150 350, 330 380, 610 560" fill="none" stroke="url(#swoop)" stroke-width="6"/>
    </svg>

    <section class="services">
      <h1>WE OFFER</h1>
      <p class="formats">1:1 SESSIONS | WORKSHOPS</p>
      <p class="corporate">CORPORATE TRAINING</p>
    </section>

    <aside class="offer-badge">
      <span class="label">offer code</span>
      <span class="code">OPENDOOR</span>
      <span class="amount">15% OFF</span>
      <span class="terms">THE BOOKERS FIRST<br>1:1 SESSION</span>
    </aside>

    <div class="call-to-action">
      <p class="line-one">FIND OUT HOW BREATHWORK</p>
      <p class="line-two">CAN HELP YOU TODAY...</p>
    </div>

    <address class="contacts" style="font-style:normal">
      <p class="name">CAROL PENNICK (SOUTH):</p>
      <p class="phone">07700 900 318</p>
      <p class="name">ROSALIND TARROW (MIDLANDS):</p>
      <p class="phone">07700 900 742</p>
    </address>

    <ul class="social">
      <li><span class="dot"></span>/we.are.gentlywindswept</li>
      <li><span class="dot"></span>@gentlywindswept</li>
    </ul>

    <p class="address">14 FERNMOOR ROAD, DUNMERE VALE, WESTSHIRE, DV4 2QX</p>
    <p class="website">WWW.GENTLYWINDSWEPT-EXAMPLE.CO.UK</p>

    <div class="brand-mark">
      <span class="ring"></span>
      <span class="name">Gently<br>Windswept</span>
    </div>
  </main>
</body>
</html>
```